Visitenkarten-Design für Vermittlung und Verkauf von Immobilien
Perfekte Umsetzung meiner Wünsche, sowie auch selbständige Einbringung von Ideen. Sehr zu empfehlen!
Zielgruppe
Immobilien vermitteln, verkaufen

```html
<!DOCTYPE html>
<html lang="de">
<head>
<meta charset="utf-8">
<title>Loraven Immobilien – Visitenkarte</title>
<link rel="stylesheet" href="https://fonts.googleapis.com/css2?family=Michroma&display=swap">
<style>
  :root {
    --navy: #0e2842;
    --paper: #ffffff;
    --stage: #ececec;
    --cream: #f4f1e6;
    --shadow: rgba(0, 0, 0, 0.28);
  }
  * { box-sizing: border-box; margin: 0; padding: 0; }
  html, body {
    width: 1200px;
    height: 1200px;
    overflow: hidden;
    background: radial-gradient(ellipse at 50% 50%, #fafafa 0%, var(--stage) 75%);
    font-family: "Michroma", sans-serif;
  }
  .sheet {
    width: 1200px;
    height: 1200px;
    display: flex;
    align-items: center;
    justify-content: center;
    gap: 72px;
  }
  .card {
    position: relative;
    width: 500px;
    height: 290px;
    border-radius: 6px;
    box-shadow: 0 6px 14px var(--shadow);
    overflow: hidden;
  }
  .card--front { background: var(--paper); color: var(--navy); }
  .card--back {
    background: var(--navy);
    color: var(--cream);
    display: flex;
    align-items: center;
    justify-content: center;
  }
  .edge-tab {
    position: absolute;
    right: 0;
    top: 58px;
    width: 12px;
    height: 172px;
    background: var(--navy);
    border-radius: 8px 0 0 8px;
  }
  .brand {
    display: flex;
    flex-direction: column;
    align-items: center;
    text-transform: uppercase;
    line-height: 1;
  }
  .brand__mark {
    width: 14px;
    height: 14px;
    background: currentColor;
    margin-bottom: 14px;
  }
  .brand__name { letter-spacing: 0.18em; }
  .brand__tag { letter-spacing: 0.2em; margin-top: 7px; }
  .card--front .brand {
    position: absolute;
    left: 22px;
    width: 200px;
    top: 96px;
  }
  .card--front .brand__name { font-size: 16px; }
  .card--front .brand__tag { font-size: 7px; }
  .card--back .brand { margin-top: 10px; }
  .card--back .brand__mark { width: 20px; height: 20px; margin-bottom: 22px; }
  .card--back .brand__name { font-size: 22px; }
  .card--back .brand__tag { font-size: 9.5px; margin-top: 9px; }
  .contact {
    position: absolute;
    left: 276px;
    top: 98px;
    text-transform: uppercase;
  }
  .contact__name {
    font-size: 11px;
    letter-spacing: 0.04em;
    margin-bottom: 22px;
    padding-left: 32px;
  }
  .contact__name .divider {
    display: inline-block;
    width: 1px;
    height: 14px;
    background: var(--navy);
    margin: 0 5px;
    vertical-align: -3px;
  }
  .contact__lines {
    list-style: none;
    font-size: 8px;
    letter-spacing: 0.08em;
    line-height: 2.1;
  }
</style>
</head>
<body>
  <main class="sheet">
    <section class="card card--front" aria-label="Vorderseite">
      <div class="brand">
        <span class="brand__mark"></span>
        <span class="brand__name">Loraven</span>
        <span class="brand__tag">Immobilien</span>
      </div>
      <div class="contact">
        <p class="contact__name">Your Name<span class="divider"></span>CEO</p>
        <ul class="contact__lines">
          <li>Your Address</li>
          <li>Phone/Fax:614.208.3395</li>
          <li>Email:post@lorvn.com</li>
          <li>www.loraven-web.com</li>
        </ul>
      </div>
      <span class="edge-tab"></span>
    </section>

    <section class="card card--back" aria-label="Rückseite">
      <div class="brand">
        <span class="brand__mark"></span>
        <span class="brand__name">Loraven</span>
        <span class="brand__tag">Immobilien</span>
      </div>
    </section>
  </main>
</body>
</html>
```